Flyer Design

I will be hosting an event at Penrith's open workroom. Here is a link to their page http://www.theopenworkroom.com.au/events-and-workshops/whats-on-penrith/. I have attached the details of my course from their website below. I hope this is of some valuable assistance.

Florist and lover of all things gorgeous, Molly Brandt from Molly Brandt Flowers will be running this beautiful and fun workshop. Come along to learn how to make your very own floral crown. All you need to bring are some closed in shoes, an apron and an open mind ready for creativity!

Teens & adults welcome

Date 1: Saturday 11 April 2015
Time 1: 11:00-2:00pm

Date 2: Thursday 23 April 2015
Time 2: 6:00-9:00pm

Cost: $90 per person (includes materials provided – see list below)
Place: The Open Workroom, Unit 3, 17 Holloway Street Penrith
RSVP: Molly via email mollybrandtflowers@postvale.com or phone 0431 507 962

Materials provided:
• Florist scissors
• Parafilm
• Wire
• Flowers
• light snacks & refreshments

```html
<!DOCTYPE html>
<html lang="en">
<head>
<meta charset="utf-8">
<title>Floral Crowns Workshop</title>
<link rel="stylesheet" href="https://fonts.googleapis.com/css2?family=Arimo:wght@400;700&family=Sacramento&family=Architects+Daughter&display=swap">
<style>
  :root {
    --pink: #e2187f;
    --band: #e63d9c;
    --ink: #2b2b2b;
    --white: #ffffff;
    --sky-top: #f6f4f7;
    --mist-mauve: #a9a1ab;
    --mist-sage: #b8c3b4;
    --mist-blue: #9aa2b4;
  }
  html, body {
    margin: 0;
    padding: 0;
    overflow: hidden;
    background: #ffffff;
  }
  .flyer {
    position: relative;
    width: 850px;
    height: 1200px;
    overflow: hidden;
    font-family: "Arimo", "Helvetica Neue", Arial, sans-serif;
    color: var(--ink);
    background: linear-gradient(180deg, #ece7ee 0px, var(--sky-top) 120px, #fbfafb 298px, #b9b0b6 300px, var(--mist-mauve) 420px, #b4b3a6 640px, var(--mist-sage) 780px, var(--mist-blue) 1020px);
  }
  .portrait {
    position: absolute;
    left: 300px;
    top: 0;
    width: 550px;
    height: 1020px;
    background:
      radial-gradient(ellipse 260px 150px at 62% 10%, #f07aa8 0%, #f3a6c2 45%, rgba(243,166,194,0) 100%),
      radial-gradient(ellipse 200px 260px at 68% 45%, #e9c7b4 0%, #d9ad94 55%, rgba(217,173,148,0) 100%),
      linear-gradient(180deg, #e8d6d0 0%, #b88a66 35%, #a07656 60%, #c7a896 85%, #d4bfb3 100%);
    -webkit-mask-image: linear-gradient(90deg, rgba(0,0,0,0) 0%, #000 28%);
    mask-image: linear-gradient(90deg, rgba(0,0,0,0) 0%, #000 28%);
  }
  .flourish {
    position: absolute;
    left: 0;
    top: 760px;
    width: 330px;
    height: 260px;
    background: radial-gradient(ellipse at 40% 60%, rgba(255,255,255,0.35), rgba(255,255,255,0) 70%);
  }
  .title {
    position: absolute;
    left: 44px;
    top: 118px;
    margin: 0;
    font-family: "Sacramento", cursive;
    font-weight: 400;
    font-size: 84px;
    line-height: 1;
    color: var(--pink);
  }
  .subtitle {
    position: absolute;
    left: 90px;
    top: 236px;
    margin: 0;
    font-family: "Architects Daughter", cursive;
    font-weight: 400;
    font-size: 31px;
    letter-spacing: 33px;
    color: #333333;
  }
  .dates {
    position: absolute;
    left: 91px;
    top: 354px;
    font-size: 24px;
    line-height: 32px;
  }
  .dates p { margin: 0 0 32px; }
  .dates strong { font-weight: 700; }
  .intro {
    position: absolute;
    left: 91px;
    top: 568px;
    margin: 0;
    font-size: 21px;
    line-height: 26.5px;
  }
  .welcome {
    position: absolute;
    left: 91px;
    top: 937px;
    margin: 0;
    font-size: 21px;
    line-height: 26.5px;
  }
  .details {
    position: absolute;
    left: 0;
    top: 1020px;
    width: 850px;
    height: 180px;
    background: var(--band);
    color: var(--white);
    box-sizing: border-box;
    padding: 23px 0 0 91px;
    font-size: 16.5px;
    line-height: 23px;
  }
  .details p { margin: 0; }
  .details .materials { margin-top: 19px; }
  .details strong { font-weight: 700; }
</style>
</head>
<body>
<main class="flyer">
  <div class="portrait" role="img" aria-label="Photo of a young woman with long hair wearing a crown of pink and cream flowers"></div>
  <div class="flourish" role="img" aria-label="Faint white floral swirl decoration"></div>

  <h1 class="title">Floral Crowns</h1>
  <h2 class="subtitle">WORKSHOP</h2>

  <section class="dates">
    <p><strong>Date 1:</strong> Saturday 11 April 2015<br>11:00-2:00 pm</p>
    <p><strong>Date 2:</strong> Thursday 23 April 2015<br>06:00-9:00 pm</p>
  </section>

  <p class="intro">Florist and lover of all things gorgeous,<br>Molly Brandt from <strong>Molly Brandt<br>Flowers</strong> will be running this beautiful<br>and fun workshop. Come along to<br>learn how to make your very own<br>floral crown. All you need<br>to bring are some<br>closed in shoes, an<br>apron and an open<br>mind ready for<br>creativity!</p>

  <p class="welcome">Teens &amp; adults<br>welcome!</p>

  <footer class="details">
    <p><strong>Cost:</strong> $90 per person (includes materials provided – see list below)</p>
    <p><strong>Place:</strong> The Open Workroom, Unit 3, 17 Holloway Street Penrith</p>
    <p><strong>RSVP:</strong> Molly via e-mail <strong>mollybrandtflowers@postvale.com</strong> or phone <strong>0431 507 962</strong></p>
    <p class="materials"><strong>Materials provided:</strong> florist scissors, parafilm, wire, flowers, light snacks &amp; refreshments</p>
  </footer>
</main>
</body>
</html>
```